Values Statement poster template

We want to develop a poster template for our company policies and statements which promote our company values in our workplaces.
These documents are important in showing our clients, suppliers and employees who we are and what we stand for.
The graphic design will incorporate our company logo, and be bright, uplifting and inspiring, developing a graphic theme that we can utilise for other company documents. The design will graphically illustrate and support our values statement, with colour and modern design.
This values poster will be the first in a series of documents using the same theme.The format will be a4 and a3 portrait
We are an environmental service business specialising in rehabilitation and revegetation

Target Market(s)

Tier one clients in industry, Mining, Construction and agriculture

Other font styles liked:
• calibri

Requirements
Must have
• Professional , high end feel, able to read clearly on a poster
Nice to have
• graphic design elements, symbols, etc which support the message, that can be carried through to various documents such as quality, environmental, safety policies
A bright theme which ties in with our logo colours.

```html
<!DOCTYPE html>
<html lang="en">
<head>
<meta charset="utf-8">
<title>Values Statement Posters</title>
<link href="https://fonts.googleapis.com/css2?family=Bitter:wght@400;700;800&display=swap" rel="stylesheet">
<style>
  :root {
    --orange: #f37421;
    --blue: #0faec9;
    --green: #86c440;
    --white: #ffffff;
    --brand-ink: #1d7a3c;
    --page: #ffffff;
    --shadow: rgba(0, 0, 0, 0.35);
  }
  html, body {
    margin: 0;
    padding: 0;
    width: 1200px;
    height: 851px;
    overflow: hidden;
    background: var(--page);
    font-family: "Bitter", Georgia, serif;
  }
  .sheet {
    position: relative;
    width: 1200px;
    height: 851px;
  }
  .poster {
    position: absolute;
    top: 113px;
    width: 345px;
    height: 487px;
    background: var(--poster-bg);
    box-shadow: 3px 3px 0 var(--shadow);
    color: var(--white);
    overflow: hidden;
  }
  .poster--orange { left: 41px;  --poster-bg: var(--orange); --value-bg: var(--blue); }
  .poster--blue   { left: 423px; --poster-bg: var(--blue);   --value-bg: var(--green); }
  .poster--green  { left: 813px; --poster-bg: var(--green);  --value-bg: var(--orange); }

  .poster__title {
    position: absolute;
    left: 30px;
    top: 30px;
    margin: 0;
    font-weight: 800;
    font-size: 28px;
    line-height: 32px;
  }
  .poster__subtitle {
    position: absolute;
    left: 30px;
    top: 101px;
    margin: 0;
    font-weight: 400;
    font-size: 13.5px;
  }
  .poster__lead {
    position: absolute;
    left: 193px;
    top: 106px;
    margin: 0;
    font-weight: 700;
    font-size: 7.5px;
  }
  .poster__symbol {
    position: absolute;
    left: 41px;
    top: 187px;
    width: 105px;
    height: 142px;
    border-radius: 50px;
    background: rgba(255, 255, 255, 0.18);
  }
  .values {
    list-style: none;
    margin: 0;
    padding: 0;
  }
  .value {
    position: absolute;
    left: 185px;
    width: 130px;
    box-sizing: border-box;
    padding: 0 6px 0 20px;
    display: flex;
    align-items: center;
    background: var(--value-bg);
    border-radius: 3px;
    font-weight: 700;
    font-size: 7px;
    line-height: 9px;
  }
  .value::before {
    content: "";
    position: absolute;
    left: 9px;
    top: 8px;
    bottom: 8px;
    width: 1.5px;
    background: var(--white);
  }
  .value--1 { top: 145px; height: 52px; }
  .value--2 { top: 210px; height: 34px; }
  .value--3 { top: 257px; height: 37px; }
  .value--4 { top: 307px; height: 37px; }
  .value--5 { top: 354px; height: 34px; }

  .brand {
    position: absolute;
    left: 185px;
    top: 445px;
    width: 130px;
    height: 42px;
    background: var(--white);
    border-radius: 5px 5px 0 0;
    display: flex;
    align-items: center;
    justify-content: center;
    gap: 5px;
  }
  .brand__dot {
    width: 8px;
    height: 8px;
    border-radius: 50%;
    background: var(--brand-ink);
  }
  .brand__name {
    color: var(--brand-ink);
    font-weight: 700;
    font-size: 13px;
  }
</style>
</head>
<body>
<main class="sheet">

  <article class="poster poster--orange">
    <h1 class="poster__title">We value<br>our people</h1>
    <p class="poster__subtitle">above everything else.</p>
    <p class="poster__lead">We demonstrate this by:</p>
    <div class="poster__symbol" role="img" aria-label="Icon of a person framed by radiating arcs"></div>
    <ul class="values">
      <li class="value value--1">Providing safe, positive, enjoyable workplaces where everyone feels valued and respected</li>
      <li class="value value--2">Providing Careers, not Jobs, we grow together</li>
      <li class="value value--3">Encouraging inclusion, participation and collaboration</li>
      <li class="value value--4">Recognising and rewarding contribution and excellence</li>
      <li class="value value--5">Supporting our people through tough times</li>
    </ul>
    <div class="brand"><span class="brand__dot"></span><span class="brand__name">Verdanta</span></div>
  </article>

  <article class="poster poster--blue">
    <h1 class="poster__title">We value<br>our people</h1>
    <p class="poster__subtitle">above everything else.</p>
    <p class="poster__lead">We demonstrate this by:</p>
    <div class="poster__symbol" role="img" aria-label="Icon of a person framed by radiating arcs"></div>
    <ul class="values">
      <li class="value value--1">Providing safe, positive, enjoyable workplaces where everyone feels valued and respected</li>
      <li class="value value--2">Providing Careers, not Jobs, we grow together</li>
      <li class="value value--3">Encouraging inclusion, participation and collaboration</li>
      <li class="value value--4">Recognising and rewarding contribution and excellence</li>
      <li class="value value--5">Supporting our people through tough times</li>
    </ul>
    <div class="brand"><span class="brand__dot"></span><span class="brand__name">Verdanta</span></div>
  </article>

  <article class="poster poster--green">
    <h1 class="poster__title">We value<br>our people</h1>
    <p class="poster__subtitle">above everything else.</p>
    <p class="poster__lead">We demonstrate this by:</p>
    <div class="poster__symbol" role="img" aria-label="Icon of a person framed by radiating arcs"></div>
    <ul class="values">
      <li class="value value--1">Providing safe, positive, enjoyable workplaces where everyone feels valued and respected</li>
      <li class="value value--2">Providing Careers, not Jobs, we grow together</li>
      <li class="value value--3">Encouraging inclusion, participation and collaboration</li>
      <li class="value value--4">Recognising and rewarding contribution and excellence</li>
      <li class="value value--5">Supporting our people through tough times</li>
    </ul>
    <div class="brand"><span class="brand__dot"></span><span class="brand__name">Verdanta</span></div>
  </article>

</main>
</body>
</html>
```